Healthy Food Healthy Brain Rack Card

We want a new 2 page (front and page) 3.67" x 8.5" rack card. This rack card is the first of a series we are creating. We will have five more eventually.

The minimum font size for the text on the front is 11 point and also for other main body text.

Use the text on the word document.

The images and layout in the word document are just sample ideas we had.

We have a subscripton to adobe stock images so prefer to get images from there or free high quality images.

The document is for older readers. Do not put text over graphics and keep it simple and easy to read with high contrast.

We are open to any color scheme, though something that conveys fresh and healthy, is good.

We want some very simple design element(s) incorporated that convey Native American communities or heritage. But NO head dress, teepee graphics, etc.

At the top, of the first page we would like a collage of healthy food images. This can include fish, chicken, fresh vegetables, berries, brown rice, etc.

On the back side, the text below the brown box on the word document with the title "mock up" can be smaller as needed.

Please remember to include the funding statement - it can be in a very small font 6/7 point.

For more information about our project, please visit https://velmorcollective.org/mind-care/

```html
<!DOCTYPE html>
<html lang="en">
<head>
<meta charset="utf-8">
<title>Healthy Food, Healthy Brain – Rack Card</title>
<link href="https://fonts.googleapis.com/css2?family=Montserrat:wght@300;400;600;700&family=Open+Sans:ital,wght@0,400;0,600;0,700;1,400;1,600&display=swap" rel="stylesheet">
<style>
  :root {
    --page-bg: #ececec;
    --card-dark: #1b1b1b;
    --card-mid: #3a3a3a;
    --ink-light: #f2f2f2;
    --ink-muted: #d6d6d6;
    --fresh-green: #98d9a4;
    --band-clay: #c88a5f;
    --frame-line: #e6e6e6;
  }
  * { box-sizing: border-box; margin: 0; padding: 0; }
  html, body { width: 1200px; height: 794px; overflow: hidden; }
  body {
    background: var(--page-bg);
    font-family: "Open Sans", sans-serif;
    color: var(--ink-light);
    position: relative;
  }
  .rack-card {
    position: absolute;
    top: 95px;
    width: 283px;
    height: 597px;
    overflow: hidden;
    background: radial-gradient(ellipse at 50% 45%, var(--card-mid) 0%, #242424 55%, var(--card-dark) 100%);
    box-shadow: 0 14px 30px rgba(0,0,0,.25);
  }
  .card-front { left: 258px; }
  .card-back { left: 612px; }
  .frame-lines { position: absolute; inset: 0; pointer-events: none; }

  /* front */
  .food-collage {
    position: absolute; left: 0; top: 0; width: 283px; height: 150px;
    background:
      linear-gradient(180deg, rgba(0,0,0,0) 60%, #2c2c2c 100%),
      linear-gradient(100deg, #c9a47f 0%, #6f8f4a 22%, #8a3b3a 40%, #a9b38a 55%, #d78866 70%, #4c5a78 88%, #8c6a48 100%);
  }
  .front-title {
    position: absolute; left: 0; right: 0; top: 144px;
    font-family: "Montserrat", sans-serif; line-height: 1;
  }
  .front-title .line-one { position: absolute; left: 72px; top: 0; }
  .front-title .line-two { position: absolute; left: 29px; top: 24px; }
  .title-green { color: var(--fresh-green); font-weight: 700; font-size: 20px; }
  .title-white { color: var(--ink-light); font-weight: 300; font-size: 31px; }
  .front-body {
    position: absolute; left: 30px; right: 30px; top: 204px;
    text-align: center; font-size: 9.4px; line-height: 12.5px;
  }
  .front-body h3 {
    color: var(--fresh-green); font-weight: 600; font-size: 10.3px; margin: 9px 0 1px;
  }
  .step-list { list-style: none; }
  .step-list li::before { content: "• "; color: var(--fresh-green); }
  .small-changes { color: var(--fresh-green); margin-top: 9px; }
  .doctor-note {
    position: absolute; left: 20px; right: 20px; top: 469px;
    text-align: center; color: var(--fresh-green);
    font-weight: 700; font-size: 10.4px; line-height: 13.5px;
  }
  .elder-quote {
    position: absolute; left: 15px; top: 504px; width: 160px;
    font-size: 9.4px; line-height: 12.5px;
  }
  .quote-mark { color: var(--fresh-green); font-family: "Montserrat", sans-serif; font-weight: 700; font-size: 22px; line-height: 0; vertical-align: -6px; }
  .quote-source { margin-top: 10px; font-style: italic; font-weight: 600; }
  .salmon-photo {
    position: absolute; left: 168px; top: 488px; width: 115px; height: 104px;
    background: radial-gradient(ellipse at 45% 45%, #f08a5d 0%, #e0683f 45%, rgba(40,40,40,0) 75%);
  }

  /* back */
  .back-title {
    position: absolute; left: 0; right: 0; top: 28px; text-align: center;
    font-family: "Montserrat", sans-serif; font-size: 22px; color: var(--fresh-green); font-weight: 600;
  }
  .back-title .title-small { font-weight: 400; font-size: 19px; color: var(--ink-light); }
  .recipe-name {
    position: absolute; left: 0; right: 0; top: 68px; text-align: center;
    color: var(--fresh-green); font-weight: 600; font-size: 10.4px; letter-spacing: .1px;
  }
  .recipe-photo {
    position: absolute; left: 8px; top: 78px; width: 120px; height: 120px; border-radius: 50%;
    border: 3px solid #c9eccf;
    background: radial-gradient(circle at 60% 45%, #e9875f 0%, #cfd5d9 40%, #7ca25a 60%, #b9bec2 100%);
  }
  .ingredients {
    position: absolute; left: 145px; top: 96px; width: 125px;
    font-size: 9.4px; line-height: 12.4px;
  }
  .ingredients h4 { color: var(--fresh-green); font-style: italic; font-weight: 600; font-size: 9.4px; }
  .directions {
    position: absolute; left: 30px; right: 30px; top: 204px;
    text-align: center; font-size: 9.4px; line-height: 12.5px;
  }
  .culture-band {
    position: absolute; left: 0; right: 0; top: 322px; height: 71px;
    background: var(--band-clay);
    display: flex; align-items: center; justify-content: center; text-align: center;
    padding: 0 20px; font-weight: 600; font-size: 10.2px; line-height: 13.4px;
  }
  .back-footer {
    position: absolute; left: 0; right: 0; top: 393px; bottom: 0; background: #111;
  }
  .more-info {
    position: absolute; left: 8px; right: 8px; top: 10px; text-align: center;
    font-size: 8.4px; line-height: 12.5px;
  }
  .more-info .info-head { font-weight: 600; font-size: 9.4px; }
  .more-info .info-label { font-weight: 700; font-size: 7.6px; }
  .more-info .info-url { font-size: 7.6px; }
  .more-info .info-org { font-weight: 700; font-size: 7.3px; }
  .brand-mark {
    position: absolute; left: 0; right: 0; top: 121px;
    display: flex; align-items: center; justify-content: center; gap: 6px;
    font-weight: 600; font-size: 9px; color: #7fcfd4;
  }
  .brand-dot { width: 22px; height: 22px; border-radius: 50%; background: #3f8f98; }
  .funding-note {
    position: absolute; left: 32px; right: 32px; top: 153px;
    text-align: center; font-size: 5.2px; line-height: 6.7px; color: var(--ink-muted);
  }
</style>
</head>
<body>

<section class="rack-card card-front">
  <div class="food-collage" role="img" aria-label="Collage of healthy foods: chicken, vegetables, salmon steaks, berries, grains, eggs and avocado"></div>
  <svg class="frame-lines" width="283" height="597" aria-hidden="true">
    <g stroke="var(--frame-line)" stroke-width="1.2" fill="none">
      <polyline points="27,176 15,176 15,480 25,480"/>
      <polyline points="254,176 267,176 267,480 257,480"/>
    </g>
  </svg>
  <h1 class="front-title">
    <span class="line-one"><span class="title-green">Healthy</span> <span class="title-white">Food,</span></span>
    <span class="line-two"><span class="title-white">Healthy</span> <span class="title-green">Brain</span></span>
  </h1>
  <div class="front-body">
    <p>Everyone slows down as they get older, both in body and mind. Eating healthier food can help your overall health, including brain health. It may also reduce your risk for memory loss and problems thinking.</p>
    <h3>Healthier steps to protect your brain:</h3>
    <ul class="step-list">
      <li>Eat more vegetables, fruits, whole grains, and lower-fat milk</li>
      <li>Use less salt and added sugar</li>
      <li>Eat more fish, chicken, turkey, beans, and nuts</li>
      <li>Cut down on bad fats (“saturated” and trans), cholesterol, and red meat</li>
      <li>Buy fresh, not packaged food when you can</li>
      <li>Limit how much alcohol you drink</li>
      <li>Learn your daily calorie needs for your body size</li>
      <li>Take care of your mental and spiritual health to support your physical and brain health</li>
    </ul>
    <p class="small-changes">Small changes can make a big difference for better brain health.</p>
  </div>
  <p class="doctor-note">Talk to your doctor about more steps to healthier food choices.</p>
  <blockquote class="elder-quote">
    <p><span class="quote-mark">“</span> Without the elk, salmon, huckleberries, shellfish, and cedar trees we are nobody… <span class="quote-mark">”</span></p>
    <p class="quote-source">Maren Tallwater (Community Elder)</p>
  </blockquote>
  <div class="salmon-photo" role="img" aria-label="Fresh salmon fillets with rosemary and lemon"></div>
</section>

<section class="rack-card card-back">
  <svg class="frame-lines" width="283" height="597" aria-hidden="true">
    <g stroke="var(--frame-line)" stroke-width="1.2" fill="none">
      <polyline points="29,37 14,37 14,312 267,312 267,37 257,37"/>
    </g>
  </svg>
  <h2 class="back-title">Make This <span class="title-small">at</span> Home</h2>
  <p class="recipe-name">GRILLED SALMON AND VEGGIE FOIL PACKETS</p>
  <div class="recipe-photo" role="img" aria-label="Salmon with asparagus, peppers and lemon in an open foil packet"></div>
  <div class="ingredients">
    <h4>Ingredients:</h4>
    <p>Salmon, Asparagus, Red or Green Peppers (Or any seasonal vegetable), Onion, Lemon - sliced, Basil, Olive Oil, Salt and Pepper, Garlic Powder</p>
  </div>
  <p class="directions">Cut asparagus, peppers, and onion into bite-size pieces. Cut salmon into 4-6 oz pieces. Tear tin foil large enough to wrap around salmon &amp; veggies (2 layers). Add veggies and salmon to foil. Drizzle with olive oil, season with salt, pepper, basil, garlic &amp; top with a piece of sliced lemon. Wrap foil tightly around food. Grill at 400 degrees for about 20 minutes. Careful opening!</p>
  <div class="culture-band">Food &amp; drink are a source of strength and connection to community. A return to traditional food pathways and eating local, seasonal fresh foods make healthier eating easier.</div>
  <footer class="back-footer">
    <div class="more-info">
      <p class="info-head">For More Information<br>About Healthier Eating</p>
      <p class="info-label">PlateWise Guide</p>
      <p class="info-url">https://www.platewiseguide.org</p>
      <p class="info-head">About Brain Health</p>
      <p class="info-org">Velmor Collective Center for Community Brain Health</p>
      <p class="info-url">https://www.velmorbrainhealth.org</p>
      <p class="info-url">Regional Memory Care Program https://www.memorycareprogram.org/aging</p>
    </div>
    <div class="brand-mark"><span class="brand-dot"></span><span>Velmor Collective</span></div>
    <p class="funding-note">This card was made possible by a community grant from a regional health partner as part of a shared funding award totaling $250,000 fully supported by that partner. The views shared here belong to the authors and do not necessarily reflect the official position or endorsement of any funding agency.</p>
  </footer>
</section>

</body>
</html>
```